Ombrik Partnering Business Card

Hello everyone. We need a business card design that would match our logo and the theme we're trying to have for Ombrik that you can find on our website and/or Linkedin page

```html
<!DOCTYPE html>
<html lang="en">
<head>
<meta charset="utf-8">
<title>Ombrik Partnering Business Card</title>
<link href="https://fonts.googleapis.com/css2?family=Roboto:wght@400;500;700&display=swap" rel="stylesheet">
<style>
  :root {
    --canvas: #efefef;
    --paper: #f7f7f7;
    --charcoal: #2b2b2a;
    --brand-purple: #3b2a6a;
    --ink-grey: #555555;
    --rule: #c9c9c9;
    --reverse-text: #ececec;
  }
  * { margin: 0; padding: 0; box-sizing: border-box; }
  html, body {
    width: 1200px; height: 1189px; overflow: hidden;
    background: var(--canvas);
    font-family: 'Roboto', Arial, sans-serif;
  }
  .sheet {
    position: relative; width: 1200px; height: 1189px;
    display: flex; flex-direction: column; align-items: center; justify-content: center; gap: 90px;
  }
  .card {
    width: 800px; height: 457px;
    box-shadow: 0 2px 10px rgba(0,0,0,0.12);
    position: relative;
  }
  .card--back {
    background: var(--charcoal);
    display: flex; align-items: center; justify-content: center;
  }
  .brand-reverse {
    display: flex; align-items: center; gap: 18px;
    color: var(--reverse-text); font-weight: 700; font-size: 56px; letter-spacing: -0.5px;
  }
  .brand-dot {
    width: 22px; height: 22px; border-radius: 50%; background: currentColor; flex: none;
  }
  .card--front {
    background: var(--paper);
    display: flex; align-items: center;
  }
  .front-brand {
    width: 370px; display: flex; justify-content: center; align-items: center; gap: 12px;
    color: var(--brand-purple); font-weight: 700; font-size: 40px; letter-spacing: -0.3px;
  }
  .front-brand .brand-dot { width: 16px; height: 16px; }
  .divider {
    width: 1px; height: 210px; background: var(--rule);
  }
  .contact {
    padding-left: 40px; color: var(--ink-grey); font-size: 19px; line-height: 1.35;
  }
  .contact-name {
    color: var(--brand-purple); font-weight: 700; font-size: 28px; line-height: 1.1;
  }
  .contact-role { margin-bottom: 10px; }
  .contact-address { margin-bottom: 10px; }
  .contact-list { list-style: none; }
  .contact-list li { display: flex; align-items: center; gap: 10px; }
  .contact-list svg { width: 16px; height: 16px; flex: none; }
</style>
</head>
<body>
<main class="sheet">
  <section class="card card--back" aria-label="Card back">
    <div class="brand-reverse"><span class="brand-dot"></span>Ombrik Partnering</div>
  </section>

  <section class="card card--front" aria-label="Card front">
    <div class="front-brand"><span class="brand-dot"></span>Ombrik Partnering</div>
    <div class="divider"></div>
    <div class="contact">
      <p class="contact-name">Daniel REEVE</p>
      <p class="contact-role">Managing Director</p>
      <p class="contact-address">22-10 Harbor Lane<br>Linden Point, NY 11400-2210</p>
      <ul class="contact-list">
        <li>
          <svg viewBox="0 0 16 16" fill="none" stroke="#555" stroke-width="1.4"><path d="M4 1.5l2.5 3-1.5 1.5a8 8 0 0 0 5 5l1.5-1.5 3 2.5-1.5 2.5C7.5 14.5 1.5 8.5 1.5 3z"/></svg>
          000.000.0000
        </li>
        <li>
          <svg viewBox="0 0 16 16" fill="none" stroke="#555" stroke-width="1.4"><rect x="4" y="1" width="8" height="14" rx="1.5"/><line x1="7" y1="12.5" x2="9" y2="12.5"/></svg>
          000.000.0000
        </li>
        <li>
          <svg viewBox="0 0 16 16" fill="none" stroke="#555" stroke-width="1.4"><rect x="1" y="3" width="14" height="10"/><path d="M1 3l7 6 7-6"/></svg>
          daniel@ombrikpartnering.com
        </li>
        <li>
          <svg viewBox="0 0 16 16" fill="none" stroke="#555" stroke-width="1.3"><circle cx="8" cy="8" r="6.5"/><ellipse cx="8" cy="8" rx="3" ry="6.5"/><line x1="1.5" y1="8" x2="14.5" y2="8"/></svg>
          www.ombrikpartnering.com
        </li>
      </ul>
    </div>
  </section>
</main>
</body>
</html>
```